Window and GutterCleaning Flyer A5 size double sided.

We need a double sided A5 flyer. Side 1, is for window cleaning, side 2 is for gutter cleaning. Licensed by Borough of Halvern Council.
Phone number 0800 315 4720.
Business address 7 Tarnlow Brae, North Pellin Edinburgh EH14 3RW.
www.clearpane-vista-services.com
We use a LoftPro Gutter inspection Cam to view your gutters first to see if they need doing.
Window cleaning ; Professional window cleaning services, what we offer, water fed pole window cleaning able to reach windows up to 60 feet.
Conservatory cleaning.
Conservatory roof cleaning.
Fascias & Soffits cleaning.
Excellent Customer Service.
Target Market(s)
domestic houses
Industry/Entity Type
window cleaning
Look and feel
Each slider illustrates characteristics of the customer's brand and the style your logo design should communicate.

```html
<!DOCTYPE html>
<html lang="en">
<head>
<meta charset="utf-8">
<title>ClearPane Vista – Window &amp; Gutter Cleaning Flyers</title>
<link rel="stylesheet" href="https://fonts.googleapis.com/css2?family=Poppins:wght@500;600;700;800&display=swap">
<style>
  :root {
    --navy: #1e1655;
    --sky: #7fa6d8;
    --green: #2f6b2f;
    --white: #ffffff;
    --stage: #a6a6a6;
    --photo-brick: #8a5a45;
    --photo-roof: #6d6a66;
    --photo-sky: #d9dde2;
    --photo-grass: #5f8f3e;
  }
  * { box-sizing: border-box; margin: 0; padding: 0; }
  html, body { width: 1200px; height: 1117px; overflow: hidden; }
  body {
    background: var(--stage);
    font-family: "Poppins", sans-serif;
    position: relative;
  }
  .flyer {
    position: absolute;
    top: 210px;
    width: 503px;
    height: 714px;
    background: var(--white);
    overflow: hidden;
    box-shadow: 0 10px 26px rgba(0,0,0,0.28);
  }
  .flyer--window { left: 79px; }
  .flyer--gutter { left: 617px; }

  .hero { position: absolute; left: 0; top: 0; width: 503px; height: 290px; }
  .flyer--window .hero { background: linear-gradient(160deg, var(--photo-roof) 0%, var(--photo-brick) 35%, #9b6b55 60%, #5b3c33 100%); }
  .flyer--gutter .hero { background: linear-gradient(155deg, #eef0f2 0%, var(--photo-sky) 45%, #c9ccd0 70%, #7c5a48 100%); }
  .hero-wave { position: absolute; left: 0; top: 258px; width: 503px; height: 36px; }

  .brand-card {
    position: absolute; left: 324px; top: 0; width: 155px; height: 160px;
    background: var(--white);
    border-radius: 0 0 18px 18px;
    display: flex; flex-direction: column; align-items: center; justify-content: center; gap: 8px;
  }
  .brand-mark { width: 18px; height: 18px; background: var(--navy); }
  .brand-name { font-weight: 800; color: var(--navy); font-size: 21px; line-height: 1.05; text-align: center; }

  .inset-photo {
    position: absolute; left: 296px; top: 172px; width: 195px; height: 118px;
    border: 3px solid var(--white); border-radius: 14px;
  }
  .flyer--window .inset-photo { background: linear-gradient(90deg, #6f8fb0 0%, #9a6a52 45%, #c9d3dc 100%); }
  .flyer--gutter .inset-photo { background: linear-gradient(120deg, #8b8a84 0%, #5e6f3f 40%, #2e3f9a 65%, #d9d9d6 100%); }

  .title {
    position: absolute; left: 0; width: 100%; top: 305px;
    text-align: center; font-weight: 800; font-size: 37px; letter-spacing: -0.3px;
    color: var(--navy); line-height: 1.1;
  }
  .title .accent { color: var(--sky); }

  .intro {
    position: absolute; left: 36px; top: 361px; width: 194px;
    text-align: center; font-weight: 600; font-size: 15px; line-height: 1.23; color: var(--navy);
  }
  .side-photo {
    position: absolute; left: 30px; top: 447px; width: 204px; height: 130px; border-radius: 12px;
    background: linear-gradient(135deg, #a0a8b1 0%, #eef2f5 40%, #8c5a43 75%, #6b4434 100%);
  }
  .offer {
    position: absolute; left: 247px; top: 364px; width: 214px; height: 213px;
    background: var(--sky); border-radius: 14px; padding: 16px 12px 0 18px; color: var(--white);
  }
  .offer-heading { font-weight: 700; font-size: 20.5px; line-height: 1; margin-bottom: 10px; }
  .offer-list { list-style: none; }
  .offer-list li {
    position: relative; padding-left: 19px; font-size: 11.4px; font-weight: 500; line-height: 1.22;
    margin-bottom: 14px;
  }
  .offer-list li svg { position: absolute; left: 0; top: 2px; width: 10px; height: 10px; }

  .arrow-tag { position: absolute; width: 162px; height: 62px; }
  .arrow-tag text { font-family: "Poppins", sans-serif; font-weight: 600; font-size: 23px; fill: var(--white); }

  .lead {
    position: absolute; left: 240px; top: 355px; width: 220px;
    text-align: center; font-weight: 600; font-size: 13.8px; line-height: 1.28; color: var(--navy);
    letter-spacing: -0.1px;
  }
  .camera-photo {
    position: absolute; left: 27px; top: 352px; width: 206px; height: 222px;
    border-radius: 16px;
    background: linear-gradient(160deg, #2a3642 0%, #1c2229 45%, #3d5a70 70%, #14181c 100%);
  }
  .tool-photo {
    position: absolute; left: 257px; top: 437px; width: 201px; height: 148px; border-radius: 14px;
    background: linear-gradient(135deg, #7fa85a 0%, var(--photo-grass) 40%, #3a4350 75%, #8895a3 100%);
  }

  .footer-band { position: absolute; left: 0; top: 584px; width: 503px; height: 130px; }
  .contact { position: absolute; left: 34px; top: 632px; color: var(--white); }
  .phone { display: flex; align-items: center; gap: 3px; font-weight: 700; font-size: 29.5px; line-height: 1; letter-spacing: 0.2px; }
  .phone svg { width: 16px; height: 22px; }
  .web { display: flex; align-items: center; gap: 5px; font-weight: 500; font-size: 12.6px; margin-top: 5px; }
  .web svg { width: 10px; height: 10px; }
  .divider { position: absolute; left: 285px; top: 644px; width: 1px; height: 44px; background: rgba(255,255,255,0.7); }
  .address {
    position: absolute; left: 297px; top: 641px; color: var(--white);
    font-weight: 500; font-size: 10.5px; line-height: 1.35; padding-left: 13px;
  }
  .address svg { position: absolute; left: 0; top: 1px; width: 9px; height: 12px; }
  .licence {
    position: absolute; left: 298px; top: 676px;
    background: var(--sky); color: var(--white); border-radius: 8px;
    font-size: 7px; font-weight: 500; padding: 2px 6px; white-space: nowrap;
  }
</style>
</head>
<body>

<section class="flyer flyer--window">
  <div class="hero" role="img" aria-label="Photo of a cleaner in a hi-vis vest washing a conservatory with a water fed pole"></div>
  <svg class="hero-wave" viewBox="0 0 503 36" preserveAspectRatio="none" aria-hidden="true">
    <path d="M0 22 Q110 6 230 20 T503 10 V36 H0Z" fill="#fff"/>
    <path d="M20 26 Q90 14 160 24" stroke="#1e1655" stroke-width="1.4" fill="none"/>
  </svg>
  <div class="brand-card">
    <span class="brand-mark"></span>
    <span class="brand-name">ClearPane<br>Vista</span>
  </div>
  <div class="inset-photo" role="img" aria-label="Collage of a pole brush spraying water, a brick house and a window being cleaned"></div>

  <h1 class="title">WINDOW <span class="accent">CLEANING</span></h1>
  <p class="intro">We offer a high-quality, professional window cleaning service across West Edinburgh.</p>
  <div class="side-photo" role="img" aria-label="Photo of a clean white uPVC conservatory"></div>

  <div class="offer">
    <h2 class="offer-heading">WHAT WE OFFER</h2>
    <ul class="offer-list">
      <li><svg viewBox="0 0 10 10"><circle cx="5" cy="5" r="5" fill="#fff"/><path d="M2.7 5.1 L4.4 6.7 L7.4 3.4" stroke="#7fa6d8" stroke-width="1.4" fill="none"/></svg>Water fed pole window cleaning able to reach windows up to 60 feet.</li>
      <li><svg viewBox="0 0 10 10"><circle cx="5" cy="5" r="5" fill="#fff"/><path d="M2.7 5.1 L4.4 6.7 L7.4 3.4" stroke="#7fa6d8" stroke-width="1.4" fill="none"/></svg>Conservatory cleaning.</li>
      <li><svg viewBox="0 0 10 10"><circle cx="5" cy="5" r="5" fill="#fff"/><path d="M2.7 5.1 L4.4 6.7 L7.4 3.4" stroke="#7fa6d8" stroke-width="1.4" fill="none"/></svg>Conservatory roof cleaning.</li>
      <li><svg viewBox="0 0 10 10"><circle cx="5" cy="5" r="5" fill="#fff"/><path d="M2.7 5.1 L4.4 6.7 L7.4 3.4" stroke="#7fa6d8" stroke-width="1.4" fill="none"/></svg>Fascias &amp; Soffits cleaning.</li>
      <li><svg viewBox="0 0 10 10"><circle cx="5" cy="5" r="5" fill="#fff"/><path d="M2.7 5.1 L4.4 6.7 L7.4 3.4" stroke="#7fa6d8" stroke-width="1.4" fill="none"/></svg>Excellent Customer Service.</li>
    </ul>
  </div>

  <svg class="footer-band" viewBox="0 0 503 130" preserveAspectRatio="none" aria-hidden="true">
    <path d="M0 14 Q90 40 200 30 T360 20 T503 8 V130 H0Z" fill="#1e1655"/>
    <path d="M12 6 Q60 0 110 10" stroke="#1e1655" stroke-width="1.4" fill="none"/>
    <path d="M150 8 Q210 -2 260 6" stroke="#1e1655" stroke-width="1.2" fill="none"/>
    <path d="M400 2 Q450 -2 495 6" stroke="#1e1655" stroke-width="1.2" fill="none"/>
  </svg>
  <div class="contact">
    <div class="phone"><svg viewBox="0 0 16 22"><path d="M4 1 L7 5 L5 8 Q6 13 10 16 L13 14 L15 18 L12 21 Q3 17 1 6 Z" fill="#7fa6d8"/></svg>0800 315 4720</div>
    <div class="web"><svg viewBox="0 0 10 10"><circle cx="5" cy="5" r="5" fill="#7fa6d8"/></svg>www.clearpane-vista-services.com</div>
  </div>
  <span class="divider"></span>
  <p class="address"><svg viewBox="0 0 9 12"><path d="M4.5 0 A4.5 4.5 0 0 1 9 4.5 C9 7.5 4.5 12 4.5 12 C4.5 12 0 7.5 0 4.5 A4.5 4.5 0 0 1 4.5 0Z" fill="#7fa6d8"/><circle cx="4.5" cy="4.5" r="1.7" fill="#1e1655"/></svg>7 Tarnlow Brae, North Pellin<br>Edinburgh EH14 3RW.</p>
  <span class="licence">Licensed by Borough of Halvern Council</span>
</section>

<section class="flyer flyer--gutter">
  <div class="hero" role="img" aria-label="Photo looking up at a white gutter, fascia and soffit under a roof edge"></div>
  <svg class="arrow-tag" style="left:120px;top:13px" viewBox="0 0 162 62" aria-hidden="true">
    <path d="M0 14 H118 V0 L162 31 L118 62 V48 H0 L12 31 Z" fill="#2f6b2f"/>
    <text x="33" y="40">Gutter</text>
  </svg>
  <svg class="arrow-tag" style="left:69px;top:98px" viewBox="0 0 162 62" aria-hidden="true">
    <path d="M0 14 H118 V0 L162 31 L118 62 V48 H0 L12 31 Z" fill="#2f6b2f"/>
    <text x="32" y="40">Fascia</text>
  </svg>
  <svg class="arrow-tag" style="left:21px;top:189px" viewBox="0 0 162 62" aria-hidden="true">
    <path d="M0 14 H118 V0 L162 31 L118 62 V48 H0 L12 31 Z" fill="#2f6b2f"/>
    <text x="39" y="40">Soffit</text>
  </svg>
  <svg class="hero-wave" viewBox="0 0 503 36" preserveAspectRatio="none" aria-hidden="true">
    <path d="M0 22 Q110 6 230 20 T503 10 V36 H0Z" fill="#fff"/>
    <path d="M20 26 Q90 14 160 24" stroke="#1e1655" stroke-width="1.4" fill="none"/>
  </svg>
  <div class="brand-card">
    <span class="brand-mark"></span>
    <span class="brand-name">ClearPane<br>Vista</span>
  </div>
  <div class="inset-photo" role="img" aria-label="Photo of a vacuum hose clearing debris from a gutter"></div>

  <h1 class="title">GUTTER <span class="accent">CLEANING</span></h1>
  <div class="camera-photo" role="img" aria-label="Photo of a gutter inspection camera with its handheld monitor on a pole"></div>
  <p class="lead">We use a LoftPro Gutter inspection Cam to view your gutters first to see if they need doing.</p>
  <div class="tool-photo" role="img" aria-label="Photo of a gutter vacuum pole with camera reaching a roof gutter above a lawn"></div>

  <svg class="footer-band" viewBox="0 0 503 130" preserveAspectRatio="none" aria-hidden="true">
    <path d="M0 14 Q90 40 200 30 T360 20 T503 8 V130 H0Z" fill="#1e1655"/>
    <path d="M12 6 Q60 0 110 10" stroke="#1e1655" stroke-width="1.4" fill="none"/>
    <path d="M150 8 Q210 -2 260 6" stroke="#1e1655" stroke-width="1.2" fill="none"/>
    <path d="M400 2 Q450 -2 495 6" stroke="#1e1655" stroke-width="1.2" fill="none"/>
  </svg>
  <div class="contact">
    <div class="phone"><svg viewBox="0 0 16 22"><path d="M4 1 L7 5 L5 8 Q6 13 10 16 L13 14 L15 18 L12 21 Q3 17 1 6 Z" fill="#7fa6d8"/></svg>0800 315 4720</div>
    <div class="web"><svg viewBox="0 0 10 10"><circle cx="5" cy="5" r="5" fill="#7fa6d8"/></svg>www.clearpane-vista-services.com</div>
  </div>
  <span class="divider"></span>
  <p class="address"><svg viewBox="0 0 9 12"><path d="M4.5 0 A4.5 4.5 0 0 1 9 4.5 C9 7.5 4.5 12 4.5 12 C4.5 12 0 7.5 0 4.5 A4.5 4.5 0 0 1 4.5 0Z" fill="#7fa6d8"/><circle cx="4.5" cy="4.5" r="1.7" fill="#1e1655"/></svg>7 Tarnlow Brae, North Pellin<br>Edinburgh EH14 3RW.</p>
  <span class="licence">Licensed by Borough of Halvern Council</span>
</section>

</body>
</html>
```